Mezzanine Floor Manufacturer looking for a new business card design

We manufacture mezzanine floors and are providers of racking systems. We provide a range of items/services - simple rack repairs , full warehouse fit outs , manufacturer and install mezzanine floors , partitioning and large turnkey projects. Recently had a new website - www.corvane-shelving.co.uk and would like our business cards updating aswell . Our current card is single sided in the old logo colours (pdf attached) and needs updating.

Target Market(s)

We deal with large projects/ multi national companies and also smaller projects and companies throughout the UK ranging from a single warehouse to a large multi site company.

Industry/Entity Type

Business

Contact Information for Business Card

Will have job title,tel no's, email ,website address etc like example pdf

Requirements
Must have
• Hi - needs to use the colours of the logo & new website. Card needs to be professional

```html
<!DOCTYPE html>
<html lang="en">
<head>
<meta charset="utf-8">
<title>Corvane business card</title>
<link href="https://fonts.googleapis.com/css2?family=Oswald:wght@500&family=Rajdhani:wght@500;600&display=swap" rel="stylesheet">
<style>
  :root{
    --bg:#8f8f8f;
    --red:#c8282a;
    --red-dark:#a91e20;
    --red-light:#d9403c;
    --paper:#f4f3f1;
    --ink:#4a4a4a;
    --rule:#2b2b2b;
    --white:#ffffff;
  }
  *{box-sizing:border-box;margin:0;padding:0}
  html,body{width:1200px;height:800px;overflow:hidden}
  body{background:var(--bg);font-family:"Rajdhani",sans-serif;position:relative}
  .card{
    position:absolute;top:246px;width:540px;height:308px;border-radius:3px;overflow:hidden;
    box-shadow:0 6px 18px rgba(0,0,0,.28);
  }
  .card--front{left:40px;background:var(--paper)}
  .card--back{left:620px;background:linear-gradient(115deg,var(--red-dark) 0%,var(--red) 40%,var(--red-light) 55%,var(--red) 70%,var(--red-dark) 100%)}

  /* front */
  .brand{position:absolute;right:36px;top:34px;display:flex;align-items:center;gap:10px;
    font-family:"Rajdhani",sans-serif;font-weight:600;font-size:34px;letter-spacing:2px;color:var(--red)}
  .brand__dot{width:16px;height:16px;border-radius:50%;background:var(--red)}
  .person{position:absolute;left:44px;top:108px}
  .person__name{font-family:"Oswald",sans-serif;font-weight:500;font-size:27px;color:var(--ink);letter-spacing:.3px;line-height:1}
  .person__role{font-family:"Rajdhani",sans-serif;font-weight:500;font-size:19px;color:var(--red);margin-top:2px;margin-left:24px;line-height:1}
  .band{position:absolute;left:0;right:0;top:168px;bottom:0;
    background:linear-gradient(110deg,var(--red-dark) 0%,var(--red) 45%,var(--red-light) 60%,var(--red) 78%,var(--red-dark) 100%);
    border-top:4px solid var(--rule)}
  .contact{list-style:none;position:absolute;color:var(--white);font-size:20px;font-weight:500;line-height:1}
  .contact li{display:flex;align-items:center;gap:14px;margin-bottom:13px}
  .contact svg{width:16px;height:16px;flex:none}
  .contact--phones{left:60px;top:40px}
  .contact--web{right:34px;top:16px;font-size:18px}

  /* back */
  .services{position:absolute;left:0;right:0;top:72px;text-align:center;color:var(--white);
    font-family:"Rajdhani",sans-serif;font-weight:600;font-size:18px;letter-spacing:.6px;line-height:1.35}
  .address{position:absolute;left:0;right:0;top:208px;display:flex;justify-content:center;align-items:center;gap:14px;
    color:var(--white);font-size:16px;font-weight:500;line-height:1.25}
  .address svg{width:14px;height:18px;flex:none}
  .address p{text-align:center}
</style>
</head>
<body>

<section class="card card--front" aria-label="Card front">
  <div class="brand"><span class="brand__dot"></span>CORVANE</div>
  <div class="person">
    <p class="person__name">DANIEL HARTLEY</p>
    <p class="person__role">technical sales</p>
  </div>
  <div class="band">
    <ul class="contact contact--phones">
      <li><svg viewBox="0 0 16 16"><path fill="#fff" d="M3 1l3 3-1.5 2c1 2 3 4 5 5L11.5 9.5l3 3-2 2.5C7 14 2 9 1 3z"/></svg>01632 960418</li>
      <li><svg viewBox="0 0 16 16"><rect x="4" y="1" width="8" height="14" rx="1.5" fill="none" stroke="#fff" stroke-width="1.6"/><circle cx="8" cy="12.5" r="1" fill="#fff"/></svg>07700 900312</li>
      <li><svg viewBox="0 0 16 16"><rect x="4" y="1" width="8" height="4" fill="#fff"/><rect x="1" y="6" width="14" height="6" rx="1" fill="#fff"/><rect x="4" y="10" width="8" height="5" fill="#fff" stroke="#c8282a" stroke-width="1"/></svg>01632 960577</li>
    </ul>
    <ul class="contact contact--web">
      <li><svg viewBox="0 0 16 16"><rect x="1" y="3" width="14" height="10" rx="1" fill="#fff"/><path d="M1.5 3.5L8 9l6.5-5.5" fill="none" stroke="#c8282a" stroke-width="1.4"/></svg>daniel@corvane-shelving.co.uk</li>
      <li><svg viewBox="0 0 16 16"><circle cx="8" cy="8" r="7" fill="#fff"/><path d="M1 8h14M8 1c-3 3-3 11 0 14M8 1c3 3 3 11 0 14" fill="none" stroke="#c8282a" stroke-width="1"/></svg>www.corvane-shelving.co.uk</li>
    </ul>
  </div>
</section>

<section class="card card--back" aria-label="Card back">
  <div class="services">
    <p>• MEZZANINE FLOORS • CANTILEVER RACKING</p>
    <p>• PALLET RACKING • SAFETY BARRIERS • LONGSPAN SHELVING</p>
    <p>• STEEL SHELVING • PARTITIONING • TURNKEY PROJECTS</p>
  </div>
  <div class="address">
    <svg viewBox="0 0 14 18"><path fill="#fff" d="M7 0a6 6 0 0 0-6 6c0 4.5 6 12 6 12s6-7.5 6-12a6 6 0 0 0-6-6zm0 8.5A2.5 2.5 0 1 1 7 3.5a2.5 2.5 0 0 1 0 5z"/></svg>
    <p>12 Millbrook Way Harlow Gate Business<br>Park Alderton, Northshire NX4 7QT</p>
  </div>
</section>

</body>
</html>
```